Flyer Design Project

We need a flyer for a monthly event that we will be having. The flyer needs to be editable in either adobe illustrator or photoshop so that we can change the details such as the date if needed... Preferable in vector art.

Name of Event : Sandalmania

Price of Tickets: $15 Tickets- Entry fee ensures a pair of thongs upon leaving, drink specials all night and priority entry.

WHEN- FEB 20th
WHERE- Velvet Loft
DJ: Tessa Harlow
web: www.velvetloftbar.com.au
ph: 9146 3705

Drink specials from 7-9pm
$3 Pots
$4 basics
$4 kelvanos

$1 pizza from 8pm-10pm

FREE PAIR OF THONGS ON DEPARTURE

Drink specials continue throughout the night

Open 7pm-3am
Updates

Hi there,

Just to be clear, a pair of thongs isĀ referringĀ to flip flops or sandals (not underwear)... thanks

Target Market(s)

University Students 18-24 years old

Industry/Entity Type

Apartment

Requirements
Must have
• must have our logo

```html
<!DOCTYPE html>
<html lang="en">
<head>
<meta charset="utf-8">
<title>Sandalmania – Velvet Loft</title>
<link rel="stylesheet" href="https://fonts.googleapis.com/css2?family=Righteous&family=Titan+One&family=Arimo:wght@400;700&family=Kaushan+Script&display=swap">
<style>
  :root {
    --cream: #f2dcb6;
    --coral: #e8584a;
    --coral-deep: #d9473b;
    --navy: #1f2b5a;
    --navy-mid: #2c4278;
    --sky: #4fa6d8;
    --white: #ffffff;
  }
  html, body { margin: 0; padding: 0; overflow: hidden; background: var(--cream); }
  .flyer {
    position: relative;
    width: 927px;
    height: 1200px;
    overflow: hidden;
    background: var(--cream);
    font-family: "Arimo", Arial, sans-serif;
    color: var(--white);
  }
  .flyer__panel {
    position: absolute;
    inset: 16px 18px 16px 18px;
    background: radial-gradient(ellipse at 30% 30%, var(--coral) 0%, var(--coral-deep) 100%);
  }
  .flyer__waves, .flyer__sandals { position: absolute; }
  .flyer__waves { left: 18px; top: 16px; width: 891px; height: 1168px; }
  .flyer__sandals { left: 68px; top: 833px; width: 282px; height: 318px; }

  .brand {
    position: absolute;
    left: 0; right: 0; top: 28px;
    display: flex; justify-content: center; align-items: center; gap: 16px;
    font-family: "Righteous", sans-serif;
    font-size: 72px;
    color: var(--navy);
    line-height: 1;
  }
  .brand__dot { width: 22px; height: 22px; border-radius: 50%; background: var(--navy); }

  .event-title {
    position: absolute;
    left: 0; right: 0; top: 128px;
    margin: 0;
    text-align: center;
    font-family: "Righteous", sans-serif;
    font-size: 118px;
    font-weight: 400;
    line-height: 1;
    color: var(--white);
    -webkit-text-stroke: 6px var(--navy);
    paint-order: stroke fill;
    letter-spacing: 1px;
  }
  .event-tagline {
    position: absolute;
    left: 0; right: 0; top: 298px;
    margin: 0;
    text-align: center;
    font-family: "Titan One", sans-serif;
    font-size: 31px;
    letter-spacing: 1px;
    color: var(--white);
    word-spacing: 4px;
  }
  .event-date, .event-hours {
    position: absolute;
    left: 66px;
    margin: 0;
    font-family: "Titan One", sans-serif;
    color: var(--white);
    -webkit-text-stroke: 5px var(--navy);
    paint-order: stroke fill;
    line-height: 1;
  }
  .event-date { top: 378px; font-size: 74px; }
  .event-hours { top: 452px; font-size: 70px; }

  .dj {
    position: absolute;
    left: 545px; top: 368px;
    margin: 0;
    font-family: "Kaushan Script", cursive;
    font-size: 52px;
    color: var(--coral);
    -webkit-text-stroke: 5px var(--white);
    paint-order: stroke fill;
    transform: rotate(16deg);
    transform-origin: left top;
    white-space: nowrap;
  }

  .specials {
    position: absolute;
    left: 71px; top: 556px;
    width: 430px;
    font-size: 25px;
    line-height: 1.3;
  }
  .specials p { margin: 0; }
  .specials__prices { margin-top: 4px !important; }
  .specials sup { font-size: 14px; }
  .specials hr {
    border: 0; border-top: 2px solid var(--white);
    margin: 10px 0 12px;
  }

  .tickets {
    position: absolute;
    left: 345px; top: 845px;
    width: 420px;
    transform: rotate(-19deg);
    transform-origin: left top;
    color: var(--white);
  }
  .tickets__note { margin: 0 0 14px 8px; font-size: 15px; line-height: 1.25; width: 290px; }
  .tickets__price { margin: 0 0 10px 40px; font-size: 33px; font-weight: 700; }
  .tickets__phone { margin: 0 0 12px 90px; font-size: 25px; font-weight: 700; }
  .tickets__web { margin: 0 0 0 110px; font-size: 27px; font-weight: 700; white-space: nowrap; }
</style>
</head>
<body>
<main class="flyer">
  <div class="flyer__panel"></div>

  <svg class="flyer__waves" viewBox="0 0 891 1168" role="img" aria-label="Illustration of large curling ocean waves in navy and sky blue">
    <defs>
      <linearGradient id="wave-tone" x1="0" y1="0" x2="0.3" y2="1">
        <stop offset="0" stop-color="var(--sky)"/>
        <stop offset="0.45" stop-color="var(--navy-mid)"/>
        <stop offset="1" stop-color="var(--navy)"/>
      </linearGradient>
    </defs>
    <path fill="url(#wave-tone)" d="M540 30 C690 0 891 20 891 20 L891 1168 L0 1168 L0 1040 C190 960 370 880 500 790 C590 730 540 610 620 550 C700 490 600 410 680 350 C740 290 540 150 540 30 Z"/>
  </svg>

  <div class="brand"><span class="brand__dot"></span><span>Velvet Loft</span></div>

  <h1 class="event-title">Sandalmania</h1>
  <p class="event-tagline">FREE PAIR OF&nbsp;&nbsp;&nbsp;&nbsp;&nbsp;THONGS ON DEPARTURE</p>

  <p class="event-date">FEB 20th</p>
  <p class="event-hours">7pm-3am</p>

  <p class="dj">DJ Tessa Harlow</p>

  <section class="specials">
    <p>Drink specials from 7-9pm</p>
    <p class="specials__prices"><sup>$</sup>3 Pots &nbsp;•&nbsp; <sup>$</sup>4 basics &nbsp;•&nbsp; <sup>$</sup>4 kelvanos</p>
    <hr>
    <p><sup>$</sup>1 pizza from 8pm-10pm</p>
    <hr>
    <p>Drink specials continue<br>throughout the night</p>
  </section>

  <div class="flyer__sandals" role="img" aria-label="Illustration of a pair of red patterned flip-flops with blue straps" style="background: radial-gradient(ellipse at 50% 45%, #f0603e 0%, #d8402f 70%, rgba(216,64,47,0) 72%);"></div>

  <section class="tickets">
    <p class="tickets__note">Entry fee ensures a pair of thongs upon leaving, drink specials all night and priority entry.</p>
    <p class="tickets__price">Tickets $15 Each</p>
    <p class="tickets__phone">Phone 9146 3705</p>
    <p class="tickets__web">www.velvetloftbar.com.au</p>
  </section>
</main>
</body>
</html>
```